Prairie Roving Sonography
Business card etc
Prairie Roving Sonography -
Creative Brief
Professional
Gerald Marsdane
Director of Operations
5817 S Hwy 912 Ste 418-509 Pellworth, TX 75938
gerald@prairierovingsono.example
www.prairierovingsono.example
You choose color and style, feedback and comments will be left.

```html
<!DOCTYPE html>
<html lang="en">
<head>
<meta charset="utf-8">
<title>Prairie Roving Sonography – Stationery</title>
<link href="https://fonts.googleapis.com/css2?family=Montserrat:wght@400;700&display=swap" rel="stylesheet">
<style>
:root{
  --stage:#e9e9ea;
  --paper:#ffffff;
  --red:#9b1b1e;
  --navy:#1f2f5a;
  --ink:#3a3a3a;
  --muted:#8a8a8a;
  --faint:#f1f1f3;
}
html,body{margin:0;padding:0;overflow:hidden}
body{width:1200px;height:343px;background:var(--stage);font-family:"Montserrat",sans-serif;position:relative}
.piece{position:absolute;background:var(--paper);box-shadow:0 1px 3px rgba(0,0,0,.25);overflow:hidden}
.piece svg{position:absolute;inset:0;width:100%;height:100%}
.brand{position:absolute;display:flex;align-items:center;gap:4px;color:var(--red);font-weight:700;white-space:nowrap}
.brand .dot{border-radius:50%;background:var(--red);flex:none}
.caption{position:absolute;font-size:5px;color:var(--muted);text-align:center;white-space:nowrap}
.small{position:absolute;font-size:4px;line-height:1.45;color:var(--ink);white-space:nowrap}

/* master logo */
.master-logo{left:19px;top:62px;width:140px;font-size:11px;line-height:1.15;white-space:normal}
.master-logo .dot{width:16px;height:16px}
.master-tag{left:39px;top:96px;font-size:6px;color:var(--muted);position:absolute}

/* business cards */
.card{left:19px;width:137px;height:84px}
.card-1{top:139px}.card-2{top:235px}
.card .brand{left:6px;top:8px;font-size:5.5px}
.card .brand .dot{width:7px;height:7px}
.card .small{right:6px;top:20px;text-align:right}

/* letterheads */
.letterhead{top:24px;width:230px;height:283px}
.lh-1{left:168px}.lh-2{left:408px}
.letterhead .brand{left:10px;top:10px;font-size:6px}
.letterhead .brand .dot{width:9px;height:9px}
.letterhead .small.addr{right:10px;top:6px;text-align:right;color:#fff}
.letterhead .small.foot{left:0;right:0;bottom:24px;text-align:center;color:var(--muted)}

/* envelope fronts */
.envelope{left:643px;width:216px;height:100px}
.env-1{top:43px}.env-2{top:200px}
.envelope .brand{left:8px;top:28px;font-size:5.5px}
.envelope .brand .dot{width:8px;height:8px}
.envelope .small{left:8px;top:40px;color:var(--muted)}

/* envelope backs */
.env-back{left:907px;width:269px}
.back-navy{top:24px;height:84px;background:var(--navy)}
.back-red{top:125px;height:79px}
.back-white{top:221px;height:86px}
.env-back .brand{left:50%;transform:translateX(-50%);font-size:5px}
.env-back .brand .dot{width:8px;height:8px}
.back-navy .brand{top:24px;color:#fff}
.back-navy .brand .dot{background:#fff}
.back-red .brand{top:22px;color:#fff}
.back-red .brand .dot{background:#fff}
.back-white .brand{top:34px}
</style>
</head>
<body>

<div class="brand master-logo"><span class="dot"></span><span>Prairie Roving<br>Sonography</span></div>
<div class="master-tag">Stationery Concept</div>

<!-- business cards -->
<div class="piece card card-1">
  <svg viewBox="0 0 137 84" preserveAspectRatio="none"><path d="M0 62 C40 54 90 70 137 58 V84 H0Z" fill="var(--red)"/><path d="M0 60 C40 52 90 68 137 56" stroke="var(--navy)" stroke-width="1" fill="none"/></svg>
  <div class="brand"><span class="dot"></span>Prairie Roving Sonography</div>
  <div class="small"><b>Gerald Marsdane</b><br>Director of Operations<br>5817 S Hwy 912 Ste 418-509<br>Pellworth, TX 75938<br>gerald@prairierovingsono.example</div>
</div>
<div class="piece card card-2">
  <svg viewBox="0 0 137 84" preserveAspectRatio="none"><path d="M0 62 C40 54 90 70 137 58 V84 H0Z" fill="var(--red)"/><path d="M0 60 C40 52 90 68 137 56" stroke="var(--navy)" stroke-width="1" fill="none"/></svg>
  <div class="brand"><span class="dot"></span>Prairie Roving Sonography</div>
  <div class="small"><b>Gerald Marsdane</b><br>Director of Operations<br>5817 S Hwy 912 Ste 418-509<br>Pellworth, TX 75938<br>www.prairierovingsono.example</div>
</div>

<!-- letterheads -->
<div class="piece letterhead lh-1">
  <svg viewBox="0 0 230 283" preserveAspectRatio="none">
    <path d="M70 0 H230 V26 C180 32 120 14 70 0Z" fill="var(--red)"/>
    <path d="M70 0 C120 16 180 34 230 28" stroke="var(--navy)" stroke-width="1.2" fill="none"/>
    <circle cx="115" cy="140" r="30" fill="var(--faint)"/>
    <path d="M0 283 V270 C80 260 150 276 230 264 V283Z" fill="var(--red)"/>
  </svg>
  <div class="brand"><span class="dot"></span>Prairie Roving Sonography</div>
  <div class="small addr">Gerald Marsdane<br>5817 S Hwy 912 Ste 418-509<br>Pellworth, TX 75938</div>
  <div class="small foot">www.prairierovingsono.example</div>
</div>
<div class="caption" style="left:168px;width:230px;top:312px">Letterhead 01</div>

<div class="piece letterhead lh-2">
  <svg viewBox="0 0 230 283" preserveAspectRatio="none">
    <path d="M70 0 H230 V26 C180 32 120 14 70 0Z" fill="var(--red)"/>
    <path d="M70 0 C120 16 180 34 230 28" stroke="var(--navy)" stroke-width="1.2" fill="none"/>
    <circle cx="115" cy="140" r="30" fill="var(--faint)"/>
    <path d="M0 283 V262 C70 250 160 272 230 258 V283Z" fill="var(--red)"/>
  </svg>
  <div class="brand"><span class="dot"></span>Prairie Roving Sonography</div>
  <div class="small foot">5817 S Hwy 912 Ste 418-509 Pellworth, TX 75938<br>gerald@prairierovingsono.example</div>
</div>
<div class="caption" style="left:408px;width:230px;top:312px">Letterhead 02</div>

<!-- envelope fronts -->
<div class="piece envelope env-1">
  <svg viewBox="0 0 216 100" preserveAspectRatio="none"><path d="M0 0 H216 V18 C150 28 80 8 0 20Z" fill="var(--red)"/><path d="M0 22 C80 10 150 30 216 20" stroke="var(--navy)" stroke-width="1" fill="none"/></svg>
  <div class="brand"><span class="dot"></span>Prairie Roving Sonography</div>
  <div class="small">5817 S Hwy 912 Ste 418-509<br>Pellworth, TX 75938</div>
</div>
<div class="caption" style="left:643px;width:216px;top:150px">Envelope Front 01</div>

<div class="piece envelope env-2">
  <svg viewBox="0 0 216 100" preserveAspectRatio="none"><path d="M0 0 H216 V24 C150 10 80 30 0 18Z" fill="var(--red)"/><path d="M0 20 C80 32 150 12 216 26" stroke="var(--navy)" stroke-width="1" fill="none"/></svg>
  <div class="brand"><span class="dot"></span>Prairie Roving Sonography</div>
  <div class="small">5817 S Hwy 912 Ste 418-509<br>Pellworth, TX 75938</div>
</div>
<div class="caption" style="left:643px;width:216px;top:312px">Envelope Front 02</div>

<!-- envelope backs -->
<div class="piece env-back back-navy">
  <svg viewBox="0 0 269 84" preserveAspectRatio="none"><path d="M0 0 L134 46 L269 0" fill="#26386b" stroke="#3a4d85" stroke-width="1"/><path d="M0 84 L110 40 M269 84 L158 40" stroke="#2c3e72" stroke-width="1"/></svg>
  <div class="brand"><span class="dot"></span>Prairie Roving Sonography</div>
</div>
<div class="piece env-back back-red">
  <svg viewBox="0 0 269 79" preserveAspectRatio="none"><path d="M0 0 H269 L134 44Z" fill="var(--red)"/><path d="M0 79 L110 40 M269 79 L158 40" stroke="#d7d7d9" stroke-width="1"/></svg>
  <div class="brand"><span class="dot"></span>Prairie Roving Sonography</div>
</div>
<div class="piece env-back back-white">
  <svg viewBox="0 0 269 86" preserveAspectRatio="none"><path d="M0 0 L134 46 L269 0" fill="none" stroke="#c9c9cc" stroke-width="1"/><path d="M0 86 L110 42 M269 86 L158 42" stroke="#d7d7d9" stroke-width="1"/></svg>
  <div class="brand"><span class="dot"></span>Prairie Roving Sonography</div>
</div>
<div class="caption" style="left:907px;width:269px;top:312px">Envelope Back</div>

</body>
</html>
```